Korimo Business Cards

Korimo is a software startup and we are looking for business cards that help convey our employee personalities, as well as the professionalism of the company.
Our company font is Comfortaa - and the company logo is attached (we are okay having the text beside the logo if applicable) where we can find the company colour scheme. Cards can be horizontal or vertical format.
We are looking for a two sided business card - on the front we will see the personal details of the employee (name, position, email and phone number), and then on the back, we will see the business details (name and logo, address, phone number, website, email, company tagline: "Building bright, friendly software for every road ahead")
We want the design to be clean and simple, but also fun, modern, and capturing of a young startup vibe.

```html
<!DOCTYPE html>
<html lang="en">
<head>
<meta charset="utf-8">
<title>Korimo Business Cards</title>
<link href="https://fonts.googleapis.com/css2?family=Comfortaa:wght@300;400;600;700&display=swap" rel="stylesheet">
<style>
  :root {
    --stage: #544b9c;
    --card-white: #f7f7f9;
    --lavender: #bec0e1;
    --lavender-deep: #a39bce;
    --ink: #9c92cc;
    --ink-dark: #4a3f8f;
    --rule: #b9b8e0;
    --mark: #a585cc;
    --tagline: #e4e4f4;
  }
  * { margin: 0; padding: 0; box-sizing: border-box; }
  html, body {
    width: 1200px; height: 800px; overflow: hidden;
    background: var(--stage);
    font-family: "Comfortaa", sans-serif;
  }
  .sheet {
    width: 1200px; height: 800px;
    display: flex; align-items: center; justify-content: center; gap: 60px;
  }
  .card {
    position: relative;
    width: 520px; height: 300px;
    border-radius: 44px;
    overflow: hidden;
    box-shadow: 0 18px 40px rgba(20, 10, 70, 0.35);
  }

  /* Front: personal details */
  .card--front { background: var(--card-white); }
  .front__rule {
    position: absolute; left: 48px; top: 50px;
    width: 300px; height: 2px; background: var(--rule);
  }
  .front__name {
    position: absolute; left: 46px; top: 78px;
    font-size: 34px; font-weight: 700; letter-spacing: 3px;
    color: var(--ink);
  }
  .front__role {
    position: absolute; left: 48px; top: 126px;
    font-size: 14px; font-weight: 300; letter-spacing: 2.5px;
    text-transform: uppercase; color: var(--ink);
  }
  .front__brand {
    position: absolute; right: 40px; top: 112px;
    display: flex; flex-direction: column; align-items: center; gap: 8px;
  }
  .brand__dot {
    width: 28px; height: 28px; border-radius: 50%;
    background: var(--mark);
  }
  .brand__name {
    font-size: 18px; font-weight: 700; color: var(--ink-dark);
  }
  .front__contact {
    position: absolute; right: 44px; bottom: 38px;
    text-align: right; font-style: normal;
    font-size: 15px; letter-spacing: 2px; line-height: 1.9;
    color: var(--ink);
  }

  /* Back: company details */
  .card--back { background: var(--lavender); }
  .back__panel {
    position: absolute; right: 0; top: 0;
    width: 34%; height: 100%; background: var(--card-white);
  }
  .back__disc {
    position: absolute; left: 60%; top: 40px;
    width: 190px; height: 190px; border-radius: 50%;
    background: var(--card-white);
  }
  .back__symbol {
    position: absolute; left: calc(60% + 50px); top: 90px;
    width: 90px; height: 90px; border-radius: 50%;
    background: var(--mark);
  }
  .back__site {
    position: absolute; right: 26px; top: 50%;
    transform: translateY(-50%) rotate(90deg);
    font-size: 15px; font-weight: 700; letter-spacing: 1.5px;
    color: var(--ink-dark);
    width: 20px; white-space: nowrap; display: flex; justify-content: center;
  }
  .back__wordmark {
    position: absolute; left: 40px; top: 34px;
    font-size: 52px; font-weight: 700; letter-spacing: 1px;
    color: var(--lavender-deep);
  }
  .back__details {
    position: absolute; left: 42px; top: 112px;
    font-style: normal; color: #fff;
    font-size: 12.5px; letter-spacing: 1.8px; line-height: 1.6;
  }
  .back__details p + p { margin-top: 10px; }
  .back__tagline {
    position: absolute; left: 42px; bottom: 26px; width: 280px;
    font-size: 11.5px; letter-spacing: 1.8px; line-height: 1.5;
    color: var(--tagline);
  }
</style>
</head>
<body>
  <main class="sheet">
    <section class="card card--front" aria-label="Business card front">
      <div class="front__rule"></div>
      <h1 class="front__name">Maren Solte</h1>
      <p class="front__role">Marketing Specialist</p>
      <div class="front__brand">
        <span class="brand__dot"></span>
        <span class="brand__name">korimo</span>
      </div>
      <address class="front__contact">
        1-800-555-0148<br>
        maren.solte@korimo.ai
      </address>
    </section>

    <section class="card card--back" aria-label="Business card back">
      <div class="back__panel"></div>
      <div class="back__disc"></div>
      <div class="back__symbol" role="img" aria-label="Korimo brand symbol"></div>
      <div class="back__site">korimo.ai</div>
      <h2 class="back__wordmark">korimo</h2>
      <address class="back__details">
        <p>Suite 210, 88 Alder Lane,<br>Westbrook, ON K4R 1B7</p>
        <p>1-800-555-0148</p>
        <p>hello@korimo.ai</p>
      </address>
      <p class="back__tagline">“Building bright, friendly software for every road ahead”</p>
    </section>
  </main>
</body>
</html>
```